Business Card Design

Name of company: Brisk Property Maintenance.
We are a new start up business.
The company is involved in general property maintenance around residential properties and high rise apartment buildings.
We carry out all types of property maintenance such as:
*Handyman work
*Plumbing
*Painting
*Electrical
*Window cleaning
*Gardens / Landscaping

Target Market(s)

*Real Estate Agents
*Body corporate managers
*Private apartment owners

Industry/Entity Type

Property Maintenance

Requirements
Must have
• Name: Dean Malloy
Address: PO Box 3862
Carrow Hill Crossing
NSW 2089
Phone: 0431 962 305
Email: dean@briskpropertymaintenance
Website: www.briskpropertymaintenance.example.au
Nice to have
• We don't have any corporate logo so you can design what you think is appropriate

```html
<!DOCTYPE html>
<html lang="en">
<head>
<meta charset="utf-8">
<title>Brisk Property Maintenance – Business Card</title>
<link rel="stylesheet" href="https://fonts.googleapis.com/css2?family=Open+Sans:wght@400;600;700&display=swap">
<style>
  :root {
    --cyan: #1db8dc;
    --charcoal: #2a292c;
    --charcoal-light: #4a4a4e;
    --paper: #f3f4f6;
    --paper-edge: #d9dadd;
    --stage: #6e6e70;
    --white: #ffffff;
  }
  * { box-sizing: border-box; margin: 0; padding: 0; }
  html, body {
    width: 1200px; height: 1000px; overflow: hidden;
    background: var(--stage);
    font-family: "Open Sans", sans-serif;
  }
  .canvas { position: relative; width: 1200px; height: 1000px; }

  /* Front of card */
  .card-front {
    position: absolute; left: 220px; top: 60px;
    width: 620px; height: 370px;
    background: var(--paper);
    box-shadow: 0 6px 18px rgba(0,0,0,.35);
    overflow: hidden;
  }
  .front-brand-panel {
    position: absolute; left: 0; top: 0; bottom: 0; width: 290px;
    background: radial-gradient(circle at 30% 35%, var(--charcoal-light), var(--charcoal) 70%);
    display: flex; align-items: center; justify-content: center; gap: 10px;
  }
  .front-accent-band {
    position: absolute; left: 290px; top: 0; bottom: 0; width: 62px;
    background: var(--cyan);
  }
  .band-notch {
    position: absolute; left: 342px; width: 20px; height: 20px;
    border-radius: 50%; background: var(--paper);
  }
  .brand-dot { width: 22px; height: 22px; border-radius: 50%; background: var(--cyan); flex: none; }
  .brand-name {
    color: var(--white); font-weight: 400; font-size: 17px;
    letter-spacing: 1.5px; line-height: 1.25; text-transform: uppercase;
  }
  .holder {
    position: absolute; left: 378px; top: 30px; right: 0;
    color: var(--cyan);
  }
  .holder-name { font-size: 24px; font-weight: 400; line-height: 1.1; }
  .holder-name strong { font-weight: 700; }
  .holder-rule { height: 1px; background: var(--cyan); margin: 4px 0 6px; }
  .holder-title { font-size: 10px; letter-spacing: 3px; text-transform: uppercase; }
  .contact {
    position: absolute; left: 374px; top: 240px; right: 14px;
    color: var(--cyan); font-size: 11px; line-height: 1.4;
    white-space: nowrap;
  }
  .contact p { margin-bottom: 14px; }

  /* Back of card */
  .card-back {
    position: absolute; left: 410px; top: 470px;
    width: 640px; height: 360px;
    background: linear-gradient(90deg, var(--paper-edge), var(--paper) 25%, var(--paper) 75%, var(--paper-edge));
    box-shadow: 0 6px 18px rgba(0,0,0,.35);
  }
  .back-band {
    position: absolute; left: 0; right: 0; top: 128px; height: 50px;
    background: linear-gradient(90deg, var(--charcoal-light), var(--charcoal) 50%, var(--charcoal-light));
  }
  .back-badge {
    position: absolute; left: 190px; top: 104px; width: 270px; height: 84px;
    background: var(--cyan); border-radius: 14px;
    display: flex; align-items: center; justify-content: center; gap: 10px;
  }
  .back-badge .brand-dot { background: var(--white); }
  .back-badge .brand-name { font-size: 15px; }

  /* Standalone brand lockup */
  .brand-lockup {
    position: absolute; left: 40px; top: 880px;
    display: flex; align-items: center; gap: 16px;
  }
  .brand-lockup .brand-dot { width: 34px; height: 34px; }
  .brand-lockup .brand-name { font-size: 30px; letter-spacing: 3px; }
</style>
</head>
<body>
<main class="canvas">

  <section class="card-front" aria-label="Business card front">
    <div class="front-brand-panel">
      <span class="brand-dot"></span>
      <p class="brand-name">Brisk Property<br>Maintenance</p>
    </div>
    <div class="front-accent-band"></div>
    <span class="band-notch" style="top:28px"></span>
    <span class="band-notch" style="top:236px"></span>
    <span class="band-notch" style="top:282px"></span>
    <span class="band-notch" style="top:326px"></span>

    <div class="holder">
      <h1 class="holder-name">Dean<strong>Malloy</strong></h1>
      <div class="holder-rule"></div>
      <p class="holder-title">Engineer</p>
    </div>

    <div class="contact">
      <p>0431 962 305</p>
      <p>PO BOX 3862<br>Carrow Hill Crossing, NSW 2089</p>
      <p>dean@briskpropertymaintenance<br>www.briskpropertymaintenance.example.au</p>
    </div>
  </section>

  <section class="card-back" aria-label="Business card back">
    <div class="back-band"></div>
    <div class="back-badge">
      <span class="brand-dot"></span>
      <p class="brand-name">Brisk Property<br>Maintenance</p>
    </div>
  </section>

  <div class="brand-lockup">
    <span class="brand-dot"></span>
    <p class="brand-name">Brisk Property<br>Maintenance</p>
  </div>

</main>
</body>
</html>
```